Business Card Design for Law firm - already have logo

Now that we have a logo, we need a business card design - our logo is attached -it is salaryman font if that helps - we would like a file that can be uploaded to cardquill (www.cardquill-example.com) using the logo and with the following information on it:
Quenby Law Firm, P.C.
Delwyn Quenby, Esq.
5817 SW 19th Ave.
Alderbay, OR 97590
971.555.0142 phone
971.555.0187 fax
del@quenby-example.net
Skype: delquenby
Google talk: delwyn.quenby@mailbox-example.com
Target Market(s)
our business cards are distributed to corporate executives, technology professionals and healthcare providers
Industry/Entity Type
Business
Look and feel

```html
<!DOCTYPE html>
<html lang="en">
<head>
<meta charset="utf-8">
<title>Delwyn Quenby, Esq. – Business Cards</title>
<link href="https://fonts.googleapis.com/css2?family=Tinos&display=swap" rel="stylesheet">
<style>
  :root {
    --ink: #111111;
    --paper: #ffffff;
    --mint-light: #eef8f6;
    --mint: #c4e8e6;
    --edge: #8a8a8a;
  }
  * { margin: 0; padding: 0; box-sizing: border-box; }
  html, body {
    width: 1200px; height: 312px; overflow: hidden;
    background: var(--paper);
    font-family: "Tinos", "Liberation Serif", "Times New Roman", serif;
    color: var(--ink);
  }
  .sheet { position: relative; width: 1200px; height: 312px; }
  .card { position: absolute; top: 0; height: 312px; width: 560px; overflow: hidden; }
  .card--mint { left: 0; border: 1px solid var(--edge);
    background: linear-gradient(90deg, var(--mint-light), var(--mint)); }
  .card--outline { left: 640px; border: 1.5px solid var(--ink); border-radius: 14px; background: var(--paper); }
  .line { position: absolute; white-space: nowrap; font-size: 20px; line-height: 1; }
  .name { font-size: 33px; left: 0; width: 100%; text-align: center; }
  .right { text-align: right; }
  .center { left: 0; width: 100%; text-align: center; }
  .wordmark {
    position: absolute; left: 0; width: 100%;
    display: flex; align-items: center; justify-content: center;
    font-size: 92px; letter-spacing: 22px; line-height: 1;
    background: var(--paper); color: var(--ink);
  }
  .info-panel { position: absolute; left: 0; width: 100%; background: var(--paper); }
  .rule { position: absolute; left: 0; width: 100%; height: 8px; background: var(--ink); }
  .outline-top { position: absolute; left: -2px; top: -2px; width: 561px; height: 250px;
    border: 1.5px solid var(--ink); border-radius: 0 0 14px 14px; }
  .outline-bottom { position: absolute; left: 4px; top: 254px; width: 549px; height: 52px;
    border: 1.5px solid var(--ink); border-radius: 14px; }
</style>
</head>
<body>
<main class="sheet">
  <section class="card card--mint" aria-label="Business card, mint version">
    <p class="line name" style="top:16px">Delwyn Quenby, Esq.</p>
    <div class="wordmark" style="top:58px;height:132px">QUENBY</div>
    <div class="info-panel" style="top:190px;height:55px"></div>
    <p class="line" style="left:7px;top:198px">5817 SW 19th Ave.</p>
    <p class="line" style="left:7px;top:224px">Alderbay, OR 97590</p>
    <p class="line right" style="right:8px;top:196px">del@quenby-example.net</p>
    <p class="line right" style="right:8px;top:223px">skype: delquenby</p>
    <div class="rule" style="top:245px"></div>
    <p class="line center" style="top:257px">phone 971.555.0142&nbsp;&nbsp;fax 971.555.0187</p>
    <p class="line center" style="top:284px">delwyn.quenby@mailbox-example.com</p>
  </section>

  <section class="card card--outline" aria-label="Business card, outlined version">
    <div class="wordmark" style="top:0;height:135px">QUENBY</div>
    <p class="line name" style="top:145px">Delwyn Quenby, Esq.</p>
    <p class="line" style="left:7px;top:188px">5817 SW 19th Ave.</p>
    <p class="line" style="left:7px;top:215px">Alderbay, OR 97590</p>
    <p class="line right" style="right:8px;top:186px">del@quenby-example.net</p>
    <p class="line right" style="right:8px;top:213px">skype: delquenby</p>
    <div class="outline-top"></div>
    <div class="outline-bottom"></div>
    <p class="line center" style="top:258px">phone 971.555.0142&nbsp;&nbsp;fax 971.555.0187</p>
    <p class="line center" style="top:285px">delwyn.quenby@mailbox-example.com</p>
  </section>
</main>
</body>
</html>
```